Proposal Brochure for Shopfitting / Construction company

We require a proposal document (Business Capabilities) to give to customers who we are tendering to, to tell them about our business. We are a shopfitting company who complete design, fit out, project management and joinery manufacture. Please see our website www.halvenfit.com.au and use information in that. The document needs to be editable so that we can add to it. An editable template would be great. You can use a mix of our photos and stock photos if you like. Please use our logo colours. Orange, gray, black white so that it all ties in. We use Publisher and Powerpoint.

Target Market(s)

Commerical Builders, Retailers, Business

Industry/Entity Type

Construction Company

Font styles to use
Sans Serif

Colors
f37122
f68d4d
333333
5c5c5c
9d9d9d

Requirements
Must have
• Must have logo, relevant photos, use logo colours Orange, black, gray. Can you stock photos or Ones provided. Business Proposal document, about us, capabiities, services etc. Use content from our website
Nice to have
• Template to be editable

```html
<!DOCTYPE html>
<html lang="en">
<head>
<meta charset="utf-8">
<title>Halvenfit Australia – Capabilities Brochure Cover</title>
<link rel="stylesheet" href="https://fonts.googleapis.com/css2?family=Titillium+Web:wght@400;600;700&display=swap">
<style>
  :root {
    --orange: #f37122;
    --orange-light: #f68d4d;
    --charcoal: #333333;
    --grey-dark: #5c5c5c;
    --grey-mid: #9d9d9d;
    --paper: #ffffff;
    --paper-shade: #f1f1f1;
    --backdrop: #e6e6e6;
  }
  * { box-sizing: border-box; margin: 0; padding: 0; }
  html, body {
    width: 1200px; height: 804px; overflow: hidden;
    background: var(--backdrop);
    font-family: "Titillium Web", Arial, sans-serif;
  }
  .cover {
    position: absolute; left: 330px; top: 22px;
    width: 540px; height: 760px;
    background: linear-gradient(180deg, var(--paper) 0%, var(--paper-shade) 100%);
    overflow: hidden;
    box-shadow: 0 4px 18px rgba(0,0,0,0.18);
  }
  .cover__shapes { position: absolute; inset: 0; }
  .brand {
    position: absolute; top: 56px; left: 0; width: 100%;
    display: flex; justify-content: center; align-items: center; gap: 10px;
  }
  .brand__square { width: 26px; height: 26px; background: var(--orange); }
  .brand__name {
    font-weight: 600; font-size: 22px; letter-spacing: 2px;
    color: var(--grey-dark);
  }
  .cover__photo {
    position: absolute; left: 0; top: 132px; width: 540px; height: 284px;
    background: linear-gradient(160deg, #2a2a2a 0%, #6b6460 45%, #c9c4bd 75%, #8d8680 100%);
  }
  .title {
    position: absolute; top: 480px; left: 0; width: 100%;
    text-align: center; font-weight: 700; font-size: 34px; letter-spacing: 0.5px;
    color: var(--charcoal);
  }
  .title__accent { color: var(--orange); }
  .title-rule {
    position: absolute; top: 530px; left: 60px; width: 420px; height: 1px;
    background: var(--grey-dark);
  }
  .tagline {
    position: absolute; top: 538px; left: 60px; width: 420px;
    text-align: center; font-size: 13px; line-height: 18px; color: var(--charcoal);
  }
  .web {
    position: absolute; top: 628px; left: 0; width: 100%;
    text-align: center; font-size: 13px; letter-spacing: 2px; color: var(--paper);
  }
</style>
</head>
<body>
  <main class="cover">
    <svg class="cover__shapes" width="540" height="760" viewBox="0 0 540 760" aria-hidden="true">
      <polygon points="300,460 420,430 470,520" fill="#ececec"/>
      <polygon points="60,450 140,470 90,560" fill="#f3f3f3"/>
      <rect x="0" y="110" width="540" height="4" fill="var(--orange)"/>
      <polygon points="258,114 282,114 270,124" fill="var(--orange)"/>
      <rect x="0" y="122" width="540" height="2" fill="var(--orange)"/>
      <rect x="0" y="424" width="540" height="2" fill="var(--orange)"/>
      <rect x="0" y="432" width="540" height="4" fill="var(--orange)"/>
      <polygon points="258,436 282,436 270,446" fill="var(--orange)"/>
      <rect x="0" y="610" width="540" height="3" fill="var(--charcoal)"/>
      <rect x="0" y="613" width="540" height="50" fill="var(--orange)"/>
      <rect x="0" y="690" width="540" height="6" fill="var(--charcoal)"/>
      <rect x="0" y="700" width="540" height="60" fill="var(--orange)"/>
    </svg>

    <div class="brand">
      <span class="brand__square"></span>
      <span class="brand__name">HALVENFIT AUSTRALIA</span>
    </div>

    <div class="cover__photo" role="img" aria-label="Photo of a fitted-out cosmetics retail store with lit ceiling canopies, display counters and wall shelving"></div>

    <h1 class="title">HALVENFIT <span class="title__accent">AUSTRALIA</span></h1>
    <div class="title-rule"></div>
    <p class="tagline">Our aim is to provide all of our clients with piece of mind and confidence in having chosen us to deliver their store.</p>

    <p class="web">www.halvenfit.com.au</p>
  </main>
</body>
</html>
```